Smart Election Management System

At this point, ensuring the designers understand the project scope is essential for us. Thus, a web design for an interactive prototype system. Users should be able to navigate through the system to review political election results on a dashboard. The system should provide at least the following options:

President (Maps by states or provinces, and municipalities)
Senate (Map by senatorial districts)
House (Map by representative districts)
Governor (Maps by states or provinces and municipalities)
Mayor (Maps by municipalities)

Each option should display its dashboard, including a map with election results, election results forecast, turnover stats, and related graphics.

These specifications provide a comprehensive outline for developing an interactive country map system that allows users to explore election statistics, including voter turnovers, results, and forecasts. It includes country and language selection, configuration options for political parties, dashboards, previous election comparisons, turnover election day timeline, and data collection screens.
1. Country and Language Selection:
o The system should allow users to select a country from the American continent, including Caribbean countries.
o Provide options for the preferred language (Spanish, English, and Portuguese).
o Dynamically adjust the content and language based on the user's selection.
2. Interactive Map:
o Include an interactive map of the selected country.
o Users can explore election statistics by region, province, or other administrative divisions.
o Allow users to click on a region or division to view specific election statistics for that area.
3. Configuration Screen:
o Provide a configuration screen accessible to administrators for setting up the system.
o Allow administrators to define up to 5 political parties:
 Fields to specify the party's acronym or short name, symbol, and color for visual representation.
 Include fields to define the party's full name and an event description (e.g., General Election, Primary Election, etc.).
o Save the configuration settings to ensure consistency across the system.
4. Dashboard Navigation:
o Implement a user-friendly dashboard for easy navigation and access to different election races and statistics.
o Include clear menus or tabs to select the desired race (presidential, congress, or mayor) and related statistics.
5. Voter Turnover Statistics:
o Display visualizations and metrics for tracking voter turnovers:
 Total voter turnover for the current election.
 Breakdowns of voter turnovers by gender, age, and party affiliation.
 Comparison of voter turnovers between the previous election and the current election.
 Turnover election day timeline by hours, showing the number of votes cast at different times throughout the election day.
6. Election Results:
o Show election results for different races: presidential, congress, and mayor.
o Provide visualizations and metrics for the following:
 Total votes by political party or candidate.
 Comparison of previous election results and current election results.
 Election results timeline, demonstrating the progression of results over time.
7. Election Result Forecasts:
o Provide forecasted election results for each race.
o Display visualizations and metrics for the following:
 Total votes by political party or candidate in the presidential, congress, and mayoral races.
 Allow users to explore different scenarios or predictions based on available data.
8. Previous Elections Comparison:
o Include a section comparing the current election's statistics with previous elections.
o Display visualizations and metrics to demonstrate changes in voter turnovers, results, and other relevant metrics.
9. Turnout Data Collection Screens:
o Develop data collection screens for gathering information at polling places.
o Design intuitive and user-friendly interfaces for collecting voter turnout data, including age, gender, and party affiliation.

Target Market(s)

Political parties, press

Industry/Entity Type

Political campaigns

Number of Pages Required

5+ page

Requirements
Must have
• Interactive funcionality

```html
<!DOCTYPE html>
<html lang="en">
<head>
<meta charset="utf-8">
<title>Smart Election Management System – Map by States</title>
<link href="https://fonts.googleapis.com/css2?family=Oswald:wght@500;600;700&family=Roboto:ital,wght@0,400;0,500;0,700;1,400&family=Arvo:wght@400;700&display=swap" rel="stylesheet">
<style>
:root{
  --ink:#111;
  --nav:#000;
  --blue:#1a6bff;
  --red:#ff4a46;
  --chart-blue:#5256d1;
  --chart-red:#f83a4b;
  --band:#f6f6f6;
  --line:#c9c9c9;
  --muted:#8a8a8a;
  --white:#fff;
}
*{box-sizing:border-box;margin:0;padding:0}
html,body{width:1200px;height:2246px;overflow:hidden;background:var(--white)}
body{position:relative;font-family:"Roboto",sans-serif;color:var(--ink)}
.abs{position:absolute}

/* header */
.brand-mark{left:66px;top:40px;width:120px;height:120px;border:4px solid var(--blue);border-radius:6px;background:var(--red)}
.site-title{left:242px;top:92px;font-family:"Oswald",sans-serif;font-weight:700;font-size:62px;line-height:1;letter-spacing:1px;white-space:nowrap;transform:scaleY(1.05)}
.lang-menu{left:959px;top:37px;width:192px;height:232px;background:var(--white);border:1px solid #ddd;border-radius:3px;z-index:5;box-shadow:0 1px 3px rgba(0,0,0,.15);font-size:11px;font-weight:500}
.lang-menu .lm-head{padding:10px 7px 7px;font-size:11.5px;font-weight:400;border-bottom:1.5px solid var(--blue);color:#333}
.lang-menu ul{list-style:none;padding:12px 6px 0}
.lang-menu li{display:flex;align-items:center;gap:7px;height:29.5px;padding-left:8px;border-radius:4px}
.lang-menu li.active{background:#f0f0f0}
.flag{width:17px;height:11px;display:inline-block}
.flag.de{background:linear-gradient(#000 33%,#dd0000 33% 66%,#ffce00 66%)}
.flag.fr{background:linear-gradient(90deg,#1a3faa 33%,#fff 33% 66%,#e4283a 66%)}
.flag.uk{background:linear-gradient(#1a2f7a 40%,#d42030 40% 60%,#1a2f7a 60%)}
.flag.ie{background:linear-gradient(90deg,#169b62 33%,#fff 33% 66%,#ff883e 66%)}
.flag.nl{background:linear-gradient(#ae1c28 33%,#fff 33% 66%,#21468b 66%)}
.flag.at{background:linear-gradient(#ed2939 33%,#fff 33% 66%,#ed2939 66%)}

.main-nav{left:0;top:248px;width:1200px;height:69px;background:var(--nav)}
.main-nav a{position:absolute;top:20px;color:var(--white);text-decoration:none;font-size:21px;font-weight:500;letter-spacing:.2px}

.maps-menu{left:72px;top:307px;width:306px;border:1.5px solid #bbb;background:var(--white);list-style:none}
.maps-menu li{height:48.3px;line-height:46px;padding-left:18px;font-size:20.5px;border-bottom:1.5px solid #bbb}
.maps-menu li:last-child{border-bottom:none}

.section-title{font-family:"Oswald",sans-serif;font-weight:500;font-size:28px;letter-spacing:.5px;text-align:center;width:400px}

/* scoreboard */
.cand-photo{top:548px;width:93px;height:119px;border:2px solid #222;background:linear-gradient(#fff,#d9d9d9)}
.cand-num{top:560px;font-family:"Oswald",sans-serif;font-weight:500;font-size:44px;line-height:1}
.cand-name{top:573px;font-family:"Oswald",sans-serif;font-weight:600;font-size:29px;line-height:1;letter-spacing:.3px}
.blue{color:var(--blue)} .red{color:var(--red)}
.win-line{left:540px;top:576px;font-size:14.5px;width:72px;text-align:center}
.win-line::after{content:"";display:block;margin:3px auto 0;width:0;height:0;border-left:4px solid transparent;border-right:4px solid transparent;border-top:6px solid #222}
.ev-bar{left:255px;top:613px;width:642px;height:23px;border-radius:2px;overflow:hidden;background:var(--red)}
.ev-bar .fill{width:366px;height:100%;background:var(--blue)}
.ev-bar .mark{position:absolute;left:321px;top:0;width:1px;height:100%;background:#222}
.vote-stat{top:650px;font-size:16.5px}
.vote-stat b{font-weight:700}
.what{left:537px;top:663px;font-size:12.5px;font-style:italic;color:#333}
.what::before{content:"i";display:inline-block;width:10px;height:10px;border-radius:50%;background:#222;color:#fff;font-size:8px;text-align:center;line-height:10px;font-style:normal;margin-right:3px}
.split-rule{left:0;top:688px;width:1200px;height:3px;background:linear-gradient(90deg,#b9d2f5,#f2b9bd)}

/* map band */
.map-band{left:0;top:691px;width:1200px;height:626px;background:var(--band)}
.proj-title{left:488px;top:738px;font-family:"Oswald",sans-serif;font-weight:600;font-size:18px}
.proj-updated{left:448px;top:766px;font-size:10.5px;color:#555}
.legend{top:742px;display:flex;gap:3px}
.legend i{display:block;width:21px;height:14px}
.legend .hatch-b{background:repeating-linear-gradient(135deg,var(--blue) 0 2px,#9fc0ff 2px 4px)}
.legend .hatch-r{background:repeating-linear-gradient(135deg,var(--red) 0 2px,#ffb3b1 2px 4px)}
.legend-cap{top:759px;font-size:9.5px;word-spacing:6px}
.us-map{left:273px;top:807px;width:804px;height:505px;border-radius:30px 40px 60px 20px;background:linear-gradient(100deg,var(--blue) 0 22%,var(--red) 22% 55%,var(--blue) 55% 62%,var(--red) 62% 80%,var(--blue) 80%)}
.zoom{left:228px;top:809px;width:32px;height:57px;background:#fff;border:1px solid #ddd;font-size:16px;font-weight:700;text-align:center}
.zoom span{display:block;height:28px;line-height:28px}
.zoom span+span{border-top:1px solid #ddd}
.side-label{left:76px;font-size:13px;font-weight:700}
.clear-pill{left:122px;top:1043px;width:37px;height:12px;border:1px solid #ddd;border-radius:6px;font-size:6.5px;color:#bbb;text-align:center;line-height:10px}
.thumb{left:77px;width:109px;height:76px;border:1.5px solid #999;border-radius:5px;overflow:hidden;background:#fff}
.thumb .art{height:58px}
.thumb .cap{font-family:"Oswald",sans-serif;font-weight:500;font-size:12px;text-align:center;line-height:16px}

/* statistics */
.cost-chart{left:187px;top:1566px;width:660px;font-family:"Arvo",serif}
.cost-head{position:absolute;top:0;font-size:16.5px;white-space:nowrap}
.cost-head small{font-size:9.5px;color:#bbb;margin-left:5px}
.cost-row{position:absolute;left:0;height:30px;display:flex;align-items:center}
.cost-row .yr{width:55px;font-size:17px}
.cost-row .bar{display:flex;height:30px;border-left:1.5px solid #333}
.cost-row .d,.cost-row .r{height:100%;color:#fff;font-weight:700;font-size:14px;text-align:right;padding-right:8px;line-height:30px}
.cost-row .d{background:var(--chart-blue)}
.cost-row .r{background:var(--chart-red)}
.proj-note{position:absolute;left:0;top:1625px;font-size:9.5px;color:#bbb}
.swing{left:862px;top:1590px;font-family:"Arvo",serif;font-size:13px;line-height:16px;color:#333}
.swing-dot{top:1585px;width:36px;height:36px;border-radius:50%;border:3px solid}
.swing-cap{top:1623px;font-family:"Arvo",serif;font-size:7.5px;color:var(--chart-blue);width:40px;text-align:center}

.world{left:637px;top:1645px;width:380px;font-family:"Arvo",serif}
.world-head{position:relative;height:24px;font-size:10px;color:#555}
.world-head span{position:absolute;top:0}
.w-row{display:grid;grid-template-columns:217px 58px 140px;align-items:center;height:14.12px}
.w-row .l{display:flex;justify-content:flex-end;align-items:center;gap:3px;font-size:7px;color:#a6a8e6}
.w-row .l i{display:block;height:9px;background:var(--chart-blue)}
.w-row b{font-weight:400;font-size:7px;text-align:center;white-space:nowrap}
.w-row .rt{display:flex;align-items:center;gap:3px;font-size:7px;color:#f8a3ab}
.w-row .rt i{display:block;height:9px;background:var(--chart-red)}
.world-src{font-size:5.5px;color:#aaa;display:flex;justify-content:space-between;padding:3px 0 0 225px}

.polls-title{left:564px;top:1834px;font-family:"Arvo",serif;font-size:16.5px}
.polls{left:187px;top:1865px}

.footer{left:0;top:2184px;width:1200px;height:62px;background:#f2f2f2;text-align:center;line-height:62px;font-size:12.5px;font-weight:500}
</style>
</head>
<body>

<header>
  <div class="abs brand-mark" aria-hidden="true"></div>
  <h1 class="abs site-title">SMART ELECTION MANAGEMENT SYSTEM</h1>
  <div class="abs lang-menu">
    <div class="lm-head">Preferred Language</div>
    <ul>
      <li><span class="flag de"></span>Deutschland</li>
      <li class="active"><span class="flag fr"></span>France</li>
      <li><span class="flag uk"></span>United Kingdom</li>
      <li><span class="flag ie"></span>Ireland</li>
      <li><span class="flag nl"></span>Netherlands</li>
      <li><span class="flag at"></span>Österreich</li>
    </ul>
  </div>
  <nav class="abs main-nav">
    <a style="left:83px">MAPS</a>
    <a style="left:202px">LIST OF PARTIES</a>
    <a style="left:412px">TRACK VOTER’S TURNOVER</a>
    <a style="left:740px">RESULTS FORECAST</a>
    <a style="left:979px">COMPARISONS</a>
  </nav>
  <ul class="abs maps-menu">
    <li>Map by States</li>
    <li>Map by Senatorial Districts</li>
    <li>Map by Provinces</li>
    <li>Map by Municipalities</li>
  </ul>
</header>

<h2 class="abs section-title" style="left:376px;top:426px">MAP BY STATES</h2>

<section class="scoreboard">
  <div class="abs cand-photo" style="left:148px" role="img" aria-label="Portrait placeholder for Candidate A"></div>
  <div class="abs cand-num blue" style="left:255px">306</div>
  <div class="abs cand-name blue" style="left:334px">CANDIDATE A</div>
  <div class="abs win-line">270 to Win</div>
  <div class="abs cand-name red" style="left:676px">CANDIDATE B</div>
  <div class="abs cand-num red" style="left:835px">232</div>
  <div class="abs cand-photo" style="left:908px" role="img" aria-label="Portrait placeholder for Candidate B"></div>
  <div class="abs ev-bar"><div class="fill"></div><div class="mark"></div></div>
  <div class="abs vote-stat" style="left:255px"><b>51.3%</b>&nbsp;&nbsp; 81,284,666</div>
  <div class="abs what">What is this?</div>
  <div class="abs vote-stat" style="left:747px">74,224,319 &nbsp;&nbsp;<b>46.9%</b></div>
</section>
<div class="abs split-rule"></div>

<section class="abs map-band"></section>
<div class="abs proj-title">Projection</div>
<div class="abs proj-updated">Updated 10:44 a.m. ET, May. 5</div>
<div class="abs legend" style="left:615px"><i style="background:var(--blue)"></i><i class="hatch-b"></i></div>
<div class="abs legend-cap" style="left:618px">Win Flip</div>
<div class="abs legend" style="left:724px"><i style="background:var(--red)"></i><i class="hatch-r"></i></div>
<div class="abs legend-cap" style="left:727px">Win Flip</div>
<div class="abs zoom"><span>+</span><span>-</span></div>
<div class="abs us-map" role="img" aria-label="Map of the United States with each state coloured blue or red by projected winner, hatched where the seat flipped"></div>

<div class="abs side-label" style="top:843px">Maps</div>
<div class="abs thumb" style="top:862px"><div class="art" style="background:#e4e4e4" role="img" aria-label="Newsdesk projection map preview"></div><div class="cap">Newsdesk Projection</div></div>
<div class="abs thumb" style="top:944px"><div class="art" style="background:linear-gradient(110deg,#ff6b69 50%,#3f84ff 50%)" role="img" aria-label="Size of lead map preview"></div><div class="cap">Size of Lead</div></div>
<div class="abs side-label" style="top:1041px">Filters</div>
<div class="abs clear-pill">CLEAR</div>
<div class="abs thumb" style="top:1060px"><div class="art" style="background:#fff8d6" role="img" aria-label="Battleground states map preview"></div><div class="cap">Battleground</div></div>
<div class="abs thumb" style="top:1142px"><div class="art" style="background:linear-gradient(110deg,#ff6b69 50%,#3f84ff 50%)" role="img" aria-label="Flipped seats map preview"></div><div class="cap">Flipped Seats</div></div>

<h2 class="abs section-title" style="left:393px;top:1450px">RESULT STATISTICS</h2>

<section class="abs cost-chart">
  <div class="cost-head" style="left:0">Total Cost of Elections<small>Inflation adjusted</small></div>
  <div class="cost-head" style="left:338px;color:var(--chart-blue)">Democrats</div>
  <div class="cost-head" style="left:547px;color:var(--chart-red)">Republicans</div>
  <div class="cost-row" style="top:35px"><span class="yr">2020</span><div class="bar"><div class="d" style="width:383px">$8.4B</div><div class="r" style="width:219px">$4.8B</div></div></div>
  <div class="proj-note" style="top:58px">Projected</div>
  <div class="cost-row" style="top:79px"><span class="yr">2016</span><div class="bar"><div class="d" style="width:155px">$3.4B</div><div class="r" style="width:151px">$3.3B</div></div></div>
  <div class="cost-row" style="top:123px"><span class="yr">2012</span><div class="bar"><div class="d" style="width:143px">$3.1B</div><div class="r" style="width:168px">$3.7B</div></div></div>
  <div class="cost-row" style="top:167px"><span class="yr">2008</span><div class="bar"><div class="d" style="width:162px">$3.6B</div><div class="r" style="width:122px">$2.7B</div></div></div>
  <div class="cost-row" style="top:212px"><span class="yr">2004</span><div class="bar"><div class="d" style="width:134px">$2.7B</div><div class="r" style="width:123px">$2.9B</div></div></div>
  <div class="cost-row" style="top:255px"><span class="yr">2000</span><div class="bar"><div class="d" style="width:89px">$2.0B</div><div class="r" style="width:115px">$2.5B</div></div></div>
</section>

<div class="abs swing">Swing<br>States</div>
<div class="abs swing-dot" style="left:908px;border-color:var(--chart-red);background:var(--chart-red)"></div>
<div class="abs swing-dot" style="left:952px;border-color:var(--chart-blue);background:#fff"></div>
<div class="abs swing-cap" style="left:906px;color:var(--chart-red)">Ohio</div>
<div class="abs swing-cap" style="left:950px">Georgia</div>

<section class="abs world">
  <div class="world-head"><span style="left:0">How would the world vote?</span><span style="left:183px;color:var(--chart-blue)">HARLAN</span><span style="left:275px;color:var(--chart-red)">VOSS</span></div>
  <div class="w-row"><div class="l">48%<i style="width:129px"></i></div><b>All Countries</b><div class="rt"><i style="width:46px"></i>17%</div></div>
  <div class="w-row"><div class="l">73%<i style="width:196px"></i></div><b>Sweden</b><div class="rt"><i style="width:27px"></i>10%</div></div>
  <div class="w-row"><div class="l">62%<i style="width:166px"></i></div><b>Belgium</b><div class="rt"><i style="width:27px"></i>10%</div></div>
  <div class="w-row"><div class="l">62%<i style="width:166px"></i></div><b>Canada</b><div class="rt"><i style="width:32px"></i>12%</div></div>
  <div class="w-row"><div class="l">62%<i style="width:166px"></i></div><b>Germany</b><div class="rt"><i style="width:27px"></i>10%</div></div>
  <div class="w-row"><div class="l">61%<i style="width:163px"></i></div><b>Mexico</b><div class="rt"><i style="width:19px"></i>7%</div></div>
  <div class="w-row"><div class="l">61%<i style="width:163px"></i></div><b>Netherlands</b><div class="rt"><i style="width:30px"></i>11%</div></div>
  <div class="w-row"><div class="l">59%<i style="width:158px"></i></div><b>Great Britain</b><div class="rt"><i style="width:38px"></i>14%</div></div>
  <div class="w-row"><div class="l">55%<i style="width:147px"></i></div><b>Australia</b><div class="rt"><i style="width:49px"></i>18%</div></div>
  <div class="w-row"><div class="l">54%<i style="width:145px"></i></div><b>Spain</b><div class="rt"><i style="width:30px"></i>11%</div></div>
  <div class="w-row"><div class="l">52%<i style="width:139px"></i></div><b>Chile</b><div class="rt"><i style="width:49px"></i>18%</div></div>
  <div class="w-row"><div class="l">52%<i style="width:139px"></i></div><b>South Africa</b><div class="rt"><i style="width:54px"></i>20%</div></div>
  <div class="w-row"><div class="l">50%<i style="width:134px"></i></div><b>France</b><div class="rt"><i style="width:27px"></i>10%</div></div>
  <div class="w-row"><div class="l">49%<i style="width:131px"></i></div><b>Italy</b><div class="rt"><i style="width:49px"></i>18%</div></div>
  <div class="w-row"><div class="l">48%<i style="width:129px"></i></div><b>South Korea</b><div class="rt"><i style="width:49px"></i>18%</div></div>
  <div class="w-row"><div class="l">48%<i style="width:129px"></i></div><b>Peru</b><div class="rt"><i style="width:41px"></i>15%</div></div>
  <div class="w-row"><div class="l">47%<i style="width:126px"></i></div><b>Malaysia</b><div class="rt"><i style="width:22px"></i>8%</div></div>
  <div class="w-row"><div class="l">41%<i style="width:110px"></i></div><b>Argentina</b><div class="rt"><i style="width:54px"></i>20%</div></div>
  <div class="w-row"><div class="l">39%<i style="width:105px"></i></div><b>Brazil</b><div class="rt"><i style="width:54px"></i>20%</div></div>
  <div class="w-row"><div class="l">38%<i style="width:102px"></i></div><b>India</b><div class="rt"><i style="width:95px"></i>35%</div></div>
  <div class="w-row"><div class="l">34%<i style="width:91px"></i></div><b>Japan</b><div class="rt"><i style="width:46px"></i>17%</div></div>
  <div class="w-row"><div class="l">33%<i style="width:88px"></i></div><b>Hungary</b><div class="rt"><i style="width:62px"></i>23%</div></div>
  <div class="w-row"><div class="l">30%<i style="width:80px"></i></div><b>Turkey</b><div class="rt"><i style="width:73px"></i>27%</div></div>
  <div class="w-row"><div class="l">27%<i style="width:72px"></i></div><b>Poland</b><div class="rt"><i style="width:73px"></i>27%</div></div>
  <div class="w-row"><div class="l">17%<i style="width:46px"></i></div><b>Russia</b><div class="rt"><i style="width:73px"></i>27%</div></div>
  <div class="world-src"><span>Source: survey</span><span>votedata.example</span></div>
</section>

<div class="abs polls-title">National Polls</div>
<svg class="abs polls" width="500" height="180" viewBox="0 0 500 180" font-family="Arvo, serif">
  <g font-size="6" fill="#aaa">
    <text x="0" y="10">70%</text><text x="0" y="49">60</text><text x="0" y="89">50</text><text x="0" y="129">40</text><text x="0" y="170">30</text>
  </g>
  <g stroke="#eee" stroke-width="1">
    <line x1="20" y1="47" x2="470" y2="47"/><line x1="20" y1="87" x2="470" y2="87"/><line x1="20" y1="127" x2="470" y2="127"/>
    <line x1="80" y1="5" x2="80" y2="175"/><line x1="270" y1="5" x2="270" y2="175"/>
  </g>
  <rect x="20" y="72" width="445" height="22" fill="#5256d1" opacity=".08"/>
  <rect x="20" y="102" width="445" height="24" fill="#f83a4b" opacity=".08"/>
  <polyline fill="none" stroke="#5256d1" stroke-width="1.3" points="20,90 40,84 60,88 80,83 100,86 120,80 140,85 160,82 180,86 200,83 220,87 240,82 260,85 280,80 300,84 320,81 340,83 360,80 380,82 400,79 420,80 440,77 465,79"/>
  <polyline fill="none" stroke="#f83a4b" stroke-width="1.3" points="20,112 40,118 60,114 80,120 100,116 120,122 140,117 160,115 180,119 200,116 220,121 240,118 260,114 280,117 300,116 320,119 340,116 360,118 380,117 400,120 420,119 440,118 465,115"/>
  <line x1="464" y1="20" x2="464" y2="175" stroke="#999" stroke-width=".8"/>
  <text x="440" y="9" font-size="5.5" font-weight="700" fill="#333">NOV. 2 LEADER</text>
  <text x="452" y="19" font-size="7" fill="#333">Harlan</text>
  <rect x="450" y="24" width="28" height="8" fill="#fff" stroke="#aaa" stroke-width=".6"/>
  <text x="457" y="30" font-size="5.5" fill="#5256d1">+8.4</text>
  <text x="467" y="79" font-size="7.5" fill="#5256d1">Harlan</text>
  <text x="467" y="87" font-size="7.5" fill="#5256d1">51.8%</text>
  <text x="467" y="114" font-size="7.5" fill="#f83a4b">Voss</text>
  <text x="467" y="122" font-size="7.5" fill="#f83a4b">43.4%</text>
</svg>

<footer class="abs footer">Copyright &nbsp;Smart Election Management System</footer>

</body>
</html>
```